Sci fi book cover - Stonehaven

We need an eBook cover design. We'll leave the imagination to you. You can read the book description below.

Book Title: Stonehaven
Author: Miles Berry

In the distant future, scientist discover the ability to create virtual matter anywhere it is desired. As long as power is supplied, the virtual matter continues to exist. It's also possible to transmit energy and information over any distance instantly.

Anything you design can be made from virtual matter with a virtual matter generator. People called Controllers can manifest anything they imagine in virtual matter. Everyone else can send designs to virtual matter generators, which manifest the designs.

Earth is off limits to virtual matter. It is renamed to Stonehaven by its inhabitants. The world is protected from virtual matter by jamming signals, which prevent the operation of virtual matter generators. Everywhere besides Stonehaven uses virtual matter--space stations, ships, etc...

There is a conspiracy to destroy Stonehaven, because of the "backwards" beliefs of the inhabitants. These extremists believe the can gain full power for the Gleamhold party from the Stonehaven party in the Pell Conclave by destroying Stonehaven.

The book starts out with virtual matter nuclear explosions on several Stonehaven major cities. It is thought to be impossible, but someone has circumvented the virtual matter jamming signals. Chief Investigator Ravi Dunmore and Corporal Nora Fenwick investigate a rogue Controller named Vor Kel, who fancies himself as the ruler of all dark forces in the universe. Vor Kel lives in the most opulent base in the universe with walls constructed of gold, platinum, and jewels. He takes on many forms from that of a fire-breathing dragon to the ideals of human beauty. He is protected by AI virtual matter beings who are programmed to do his bidding.

They know that Vor Kel is somehow involved in the conspiracy, but they don't know how deep it goes are who else is involved. Dunmore and Fenwick visit his base undercover as space pirates in an attempt to get access to Vor Kel's supercomputer and investigate how deep the conspiracy goes.

The book is a journey of imagination, psychology, and spirituality. Will they solve the mystery, find love, and find redemption, or will everything real be destroyed?

Colors

Designer to choose colors to be used in the design.

Requirements
Nice to have
• Below are some general possibilities. The designer is completely free to depart from these ideas. Use your creativity in the way that best suits you.
• 1. People in the book have neural implants which allow them to consult internal screens, have augmented reality that allows them to see auras around certain people, or people who are virtually present, or are able to mentally select targets. You could come up with an image reflecting some of these concepts.
• 2. Image of the Earth with a glowing aura and nuclear explosions occurring with a space station in orbit.
• 3. Image of an opulent space station with a central X structure and a circular outer region. Composed of platinum, gold, and silver with inlaid jewels. Opulent, but slightly sinister.
• 4. Image of the Earth with a standard grey colored space stations (large capacity--100000 people).
• 5. Image of a woman and man who reflect ideals of human beauty who have a hint of underlying menace surrounded by classical religious paintings. The paintings exalt the man rather than traditional religious figures. This is the character of Vor Kel from the book who is human, but is a representation of Satan.

```html
<!DOCTYPE html>
<html lang="en">
<head>
<meta charset="utf-8">
<title>Stonehaven — Miles Berry</title>
<link rel="stylesheet" href="https://fonts.googleapis.com/css2?family=Josefin+Sans:wght@100;300&display=swap">
<style>
  :root {
    --backdrop: #e6d3c8;
    --cover-base: #120e14;
    --nebula-plum: #5a2440;
    --nebula-violet: #3a2242;
    --core-glow: #f3eaff;
    --spark-teal: #5fe3e0;
    --hand-red: #d8584a;
    --type-light: #eeeaf0;
  }
  html, body {
    margin: 0;
    width: 1200px;
    height: 1200px;
    overflow: hidden;
    background: var(--backdrop);
  }
  .book-cover {
    position: absolute;
    left: 185px;
    top: 30px;
    width: 830px;
    height: 1140px;
    background: var(--cover-base);
    overflow: hidden;
    box-shadow: 0 20px 40px rgba(60, 30, 30, 0.25);
  }
  .cover-art {
    position: absolute;
    inset: 0;
    background:
      radial-gradient(circle at 50% 40%, var(--core-glow) 0, rgba(243,234,255,0.55) 18px, rgba(200,120,190,0.25) 70px, transparent 160px),
      radial-gradient(circle at 90% 20%, rgba(95,227,224,0.35) 0, transparent 120px),
      radial-gradient(ellipse 220px 110px at 55% 66%, rgba(216,88,74,0.75) 0, rgba(216,88,74,0.25) 60%, transparent 100%),
      radial-gradient(ellipse 520px 420px at 35% 45%, var(--nebula-plum) 0, transparent 70%),
      radial-gradient(ellipse 500px 600px at 60% 30%, var(--nebula-violet) 0, transparent 75%),
      var(--cover-base);
  }
  .author-name {
    position: absolute;
    top: 150px;
    left: 0;
    right: 0;
    text-align: center;
    font-family: "Josefin Sans", sans-serif;
    font-weight: 100;
    font-size: 32px;
    letter-spacing: 0.55em;
    color: var(--type-light);
    margin: 0;
  }
  .book-title {
    position: absolute;
    bottom: 150px;
    left: 0;
    right: 0;
    text-align: center;
    font-family: "Josefin Sans", sans-serif;
    font-weight: 100;
    font-size: 66px;
    letter-spacing: 0.42em;
    padding-left: 0.42em;
    color: var(--type-light);
    text-shadow: 0 0 14px rgba(255,255,255,0.35);
    margin: 0;
  }
</style>
</head>
<body>
  <main class="book-cover">
    <div class="cover-art" role="img" aria-label="Space illustration: two mechanical generators fire energy beams at a small glowing Earth caught in lightning, above an open red human hand, against a purple starfield"></div>
    <p class="author-name">MILES BERRY</p>
    <h1 class="book-title">STONEHAVEN</h1>
  </main>
</body>
</html>
```